New Property management company business cards

Looking for a new business card, to reflect new younger ownership
Card should be clean, simple and professional but with a modern layout that is conveys our new logo and business model

Key aspects of the business:

Property Management
Facility Maintenance
Project Management
Tenant Improvements

Mailing Address:
PO BOX 7186
Ferrow CA, 95418

Phone: 209-614-8837
Direct: 209-614-8831

Doyle Farrant
President

Target Market(s)

Commercial property owners

Industry/Entity Type

Real Estate property management

Contact Information for Business Card

Open to all designs but lean toward vertical layouts

Requirements
Must have
• Logo and space to customize name and contact info

```html
<!DOCTYPE html>
<html lang="en">
<head>
<meta charset="utf-8">
<title>Valmora Property Management — Business Cards</title>
<link rel="stylesheet" href="https://fonts.googleapis.com/css2?family=Marcellus+SC&family=Raleway:wght@300;400&display=swap">
<style>
  :root {
    --bg: #d6d6d8;
    --card: #ffffff;
    --teal: #3fd1c8;
    --teal-soft: #e3f6f5;
    --slate: #575a68;
    --grey-band: #e6e6e9;
    --ink: #6b6d76;
  }
  * { box-sizing: border-box; margin: 0; padding: 0; }
  html, body { width: 1200px; height: 900px; overflow: hidden; }
  body {
    background: var(--bg);
    display: flex;
    align-items: center;
    justify-content: center;
    gap: 56px;
  }
  .card {
    position: relative;
    width: 530px;
    height: 303px;
    background: var(--card);
    overflow: hidden;
    box-shadow: 0 14px 30px rgba(0,0,0,0.18);
  }
  .card-decor { position: absolute; inset: 0; width: 100%; height: 100%; }

  /* Front */
  .brand {
    position: absolute; left: 30px; top: 26px;
    display: flex; align-items: center; gap: 10px;
    font-family: "Marcellus SC", serif; color: var(--slate);
  }
  .brand-square { width: 16px; height: 16px; background: var(--teal); }
  .brand-name { font-size: 22px; letter-spacing: 3px; line-height: 1; }
  .brand-sub { font-size: 8px; letter-spacing: 2.6px; margin-top: 3px; }
  .person { position: absolute; left: 30px; top: 76px; font-family: "Raleway", sans-serif; }
  .person-name { font-size: 22px; font-weight: 400; color: var(--slate); }
  .person-title { font-size: 15px; font-weight: 300; color: var(--teal); }
  .rule { position: absolute; left: 30px; right: 20px; top: 142px; height: 1px; background: var(--teal); }
  .services {
    position: absolute; right: 24px; top: 32px; list-style: none; text-align: right;
    font-family: "Marcellus SC", serif; font-size: 15px; line-height: 19px; color: var(--teal);
  }
  .contact, .address {
    position: absolute; top: 158px;
    font-family: "Marcellus SC", serif; font-size: 14px; line-height: 19px; color: var(--ink);
  }
  .contact { left: 30px; }
  .address { right: 24px; text-align: right; }
  .label { color: var(--teal); }

  /* Back */
  .card-back { border: 8px solid var(--teal); }
  .back-brand {
    position: absolute; left: 0; right: 0; top: 50%; transform: translateY(-50%);
    display: flex; flex-direction: column; align-items: center; gap: 10px;
    font-family: "Marcellus SC", serif; color: var(--slate);
  }
  .back-brand .brand-square { width: 34px; height: 34px; }
  .back-brand .brand-name { font-size: 40px; letter-spacing: 7px; }
  .back-brand .brand-sub { font-size: 12px; letter-spacing: 5px; }
</style>
</head>
<body>

  <article class="card card-front">
    <svg class="card-decor" viewBox="0 0 530 303" aria-hidden="true">
      <polygon points="0,70 70,0 110,0 0,110" fill="var(--teal-soft)"/>
      <polygon points="150,0 200,0 230,40 180,40" fill="var(--grey-band)" opacity="0.7"/>
      <polygon points="300,303 420,220 470,220 350,303" fill="var(--grey-band)"/>
      <polygon points="400,303 480,250 530,250 530,262 460,303" fill="var(--teal-soft)"/>
    </svg>
    <div class="brand">
      <span class="brand-square"></span>
      <div>
        <div class="brand-name">VALMORA</div>
        <div class="brand-sub">PROPERTY MANAGEMENT</div>
      </div>
    </div>
    <div class="person">
      <p class="person-name">Doyle Farrant</p>
      <p class="person-title">President</p>
    </div>
    <ul class="services">
      <li>Property Management</li>
      <li>Facility Maintenance</li>
      <li>Project Management</li>
      <li>Tenant Improvements</li>
    </ul>
    <div class="rule"></div>
    <div class="contact">
      <p><span class="label">Phone:</span> 209-614-8837</p>
      <p>Direct: 209-614-8831</p>
    </div>
    <div class="address">
      <p><span class="label">Mailing Address:</span> PO BOX 7186</p>
      <p>Ferrow CA, 95418</p>
    </div>
  </article>

  <article class="card card-back">
    <svg class="card-decor" viewBox="0 0 514 287" preserveAspectRatio="none">
      <polygon points="0,140 0,287 120,287" fill="var(--teal-soft)" role="img" aria-label="Teal dot pattern area"/>
      <polygon points="514,0 390,0 514,150" fill="var(--teal-soft)" role="img" aria-label="Teal dot pattern area"/>
    </svg>
    <div class="back-brand">
      <span class="brand-square"></span>
      <div class="brand-name">VALMORA</div>
      <div class="brand-sub">PROPERTY MANAGEMENT</div>
    </div>
  </article>

</body>
</html>
```